Design a logo and labels for a brewery

This contest is for a logo and four labels for four different types of bottled beers listed below utilizing the logo.

The Valmor Brewing Co. is a new production brewery opening in Mobile, AL late 2014. We want to be the Lumeta of the craft beer market. Mobile is located next to Mobile Bay, the Delta, many rivers and the Gulf of Mexico. Boating, fishing and going to the beach is our lifestyle and we want an image that captures this lifestyle. We want to be the beer people put in their Brakko coolers while they are wearing their Venholt fishing shirt and Punta Ravel sunglasses driving around in their trucks with a Reef Daze bumper sticker trailering their Skimrunner center console fishing boat. I want a logo that captures this gulf coast lifestyle that is instantly recognizable from a distance along with labels for our bottles. We will launch with four year long beers that are tentatively named Net & Reel Lager, Sandspit IPA, Dune Wake Porter (the prop of a boat motor, not airplane) and Marsh Breeze Wheat. We will also have three seasonal beers along with a selection of beers only available in the taproom. These names are not set in stone and can be changed. I want the image to be consistent throughout the entire line of beers and also throughout our merchandise, i.e. t-shirts, koozies, bottle openers, etc.

The images included are some things that have stuck out to us.

1) The image below with "Redgill" on it is a picture of a real boat named Redgill that was docked at a marina. I liked the way it was written because if this were a logo it would be the name and the logo in one. Good logos are instantly recognized without the name but a logo that is also the name like Zuma-Fizz, ParQo and Reef Daze are even better. I also liked that is was on the back of a boat.

2.) The images for the Bog Lantern Brewery did a great job depicting the environment in Florida and I like the consistency among the line.

3.) The image of the Skimrunner fishing boat is the typical recreational fishing boat in our area.

```html
<!DOCTYPE html>
<html lang="en">
<head>
<meta charset="utf-8">
<title>The Valmor Brewing Co. — Net &amp; Reel Lager Label</title>
<link rel="stylesheet" href="https://fonts.googleapis.com/css2?family=Alfa+Slab+One&family=Oswald:wght@400;600&display=swap">
<style>
  :root {
    --backdrop: #6e6660;
    --backdrop-light: #8a827b;
    --label-blue: #2c9fd3;
    --label-blue-deep: #1a7fb0;
    --field-gold: #e6c77a;
    --field-cream: #f1e3b3;
    --panel-teal: #1f3b45;
    --ink-teal: #1c3943;
    --ink-light: #dfe9ec;
    --title-blue: #6fc3e6;
    --white: #ffffff;
  }
  * { box-sizing: border-box; margin: 0; padding: 0; }
  html, body { width: 1200px; height: 799px; overflow: hidden; }
  body {
    background: radial-gradient(ellipse at 50% 35%, var(--backdrop-light), var(--backdrop) 75%);
    font-family: "Oswald", sans-serif;
    position: relative;
  }

  /* Brand name block */
  .brand-mark {
    position: absolute;
    top: 110px; left: 0; width: 1200px;
    display: flex; align-items: center; justify-content: center; gap: 18px;
  }
  .brand-mark__dot {
    width: 34px; height: 34px; border-radius: 50%;
    background: var(--label-blue);
  }
  .brand-mark__name {
    font-family: "Oswald", sans-serif;
    font-weight: 600; font-size: 46px; letter-spacing: 1px;
    color: var(--field-cream); text-transform: uppercase;
  }

  /* Flat bottle label */
  .label {
    position: absolute;
    left: 150px; top: 290px; width: 900px; height: 320px;
    background: var(--label-blue);
    padding: 10px 0 0;
  }
  .label__field {
    position: absolute; left: 0; top: 10px; width: 900px; height: 252px;
    background: linear-gradient(120deg, var(--field-cream), var(--field-gold) 55%, var(--field-cream));
  }
  .label__story {
    position: absolute; left: 22px; top: 22px; width: 160px; height: 228px;
    background: var(--panel-teal);
    color: var(--ink-light);
    padding: 12px 12px;
  }
  .label__story-title {
    font-family: "Alfa Slab One", serif;
    font-size: 17px; line-height: 1; color: var(--title-blue);
    text-align: center; margin-bottom: 10px;
  }
  .label__story p {
    font-size: 6.2px; line-height: 1.35; text-transform: uppercase;
    margin-bottom: 7px; letter-spacing: 0.2px;
  }
  .label__story-sign {
    position: absolute; left: 0; bottom: 12px; width: 100%;
    text-align: center; text-transform: uppercase;
  }
  .label__story-sign small { display: block; font-size: 6px; margin-bottom: 3px; }
  .label__story-sign strong { font-weight: 400; font-size: 10px; }

  .label__brand {
    position: absolute; left: 300px; top: 38px; width: 400px;
    display: flex; align-items: center; justify-content: center; gap: 10px;
  }
  .label__brand-dot { width: 18px; height: 18px; border-radius: 50%; background: var(--label-blue); }
  .label__brand-name {
    font-family: "Oswald", sans-serif; font-weight: 600; font-size: 22px;
    color: var(--ink-teal); text-transform: uppercase;
  }

  .label__title {
    position: absolute; left: 260px; top: 100px; width: 480px;
    font-family: "Alfa Slab One", serif; color: var(--ink-teal);
    text-align: center; text-transform: uppercase; line-height: 0.95;
  }
  .label__title-top { display: block; font-size: 50px; }
  .label__title-main { display: block; font-size: 66px; }

  .label__volume {
    position: absolute; left: 720px; top: 222px;
    font-size: 18px; color: var(--ink-teal);
  }

  .label__side {
    position: absolute; right: 22px; top: 22px; width: 70px; height: 228px;
    background: var(--panel-teal);
    display: flex; align-items: center; justify-content: center;
  }
  .label__side p {
    writing-mode: vertical-rl; transform: rotate(180deg);
    color: var(--ink-light); font-size: 6.2px; line-height: 1.4;
    text-transform: uppercase; height: 210px;
  }

  .label__footer {
    position: absolute; left: 0; bottom: 0; width: 900px; height: 58px;
    background: var(--label-blue-deep);
    text-align: center; color: var(--white); text-transform: uppercase;
    padding-top: 10px;
  }
  .label__footer strong { display: block; font-weight: 600; font-size: 15px; letter-spacing: 0.5px; }
  .label__footer span { display: block; font-size: 10px; }
</style>
</head>
<body>

  <div class="brand-mark">
    <span class="brand-mark__dot"></span>
    <span class="brand-mark__name">The Valmor Brewing Co.</span>
  </div>

  <section class="label">
    <div class="label__field" role="img" aria-label="Gold and cream textured background with pale blue wave patterns"></div>

    <div class="label__story">
      <h2 class="label__story-title">Net &amp; Reel<br>Lager</h2>
      <p>Brewed slowly on the coast with pale malt, crisp hops and clean water. A light golden lager made for long days on the boat and cool nights by the bay shore.</p>
      <p>Pour it cold into a tall glass and share it with friends after a good day of fishing on open water.</p>
      <p>Keep it on ice in the cooler and enjoy it fresh under the warm sun.</p>
      <div class="label__story-sign">
        <small>Something cool in 1929's</small>
        <strong>The Valmor Brewing Co.</strong>
      </div>
    </div>

    <div class="label__brand">
      <span class="label__brand-dot"></span>
      <span class="label__brand-name">The Valmor Brewing Co.</span>
    </div>

    <h1 class="label__title">
      <span class="label__title-top">Net &amp; Reel</span>
      <span class="label__title-main">Lager</span>
    </h1>

    <div class="label__volume">350ml</div>

    <div class="label__side">
      <p>Brewed and bottled by the brewery. Please drink responsibly and recycle this bottle after use. Best served cold.</p>
    </div>

    <div class="label__footer">
      <strong>Premium quality beer from Costa Rica</strong>
      <span>With the absolute freshness of the 1990's</span>
    </div>
  </section>

</body>
</html>
```